Kelmor Construct Inc. Business cards and Stationary
Kelmor Construct Inc
Kelmor Construct Inc. Business cards and Stationary - Construction
Creative Brief
Professional
Dean T. Haskel
President
12 Example Lane, Springdale, ST 00000
Dean@kelmorconstructinc.example
www.kelmorconstructinc.example
Kelmor Construct is a construction company the handles everything from design to delivery of buildings, homes, renovations for both the commercial and residential market. Need to convey strength, durability, honesty, integrity and being a partner in the a customer's diverse project from luxury home to brick and mortar.
Logo on back (possibly)

```html
<!DOCTYPE html>
<html lang="en">
<head>
<meta charset="utf-8">
<title>Kelmor Construct Inc. — Stationery Set</title>
<link href="https://fonts.googleapis.com/css2?family=Montserrat:wght@400;600;700&display=swap" rel="stylesheet">
<style>
  :root{
    --bg:#e6e8ec;
    --paper:#ffffff;
    --blue:#1c48b0;
    --navy:#0a2468;
    --deep:#061a4f;
    --light:#5d8be0;
    --ink:#2b3444;
    --muted:#8a93a3;
  }
  *{box-sizing:border-box;margin:0;padding:0}
  html,body{width:1200px;height:228px;overflow:hidden}
  body{background:var(--bg);font-family:"Montserrat",Arial,sans-serif;color:var(--ink);position:relative}
  .item{position:absolute;box-shadow:0 1px 3px rgba(0,0,0,.18)}
  .brand{display:flex;align-items:center;gap:3px;font-weight:600;white-space:nowrap}
  .brand .dot{border-radius:50%;background:currentColor;display:inline-block;flex:none}
  .swoosh{position:absolute;left:0;right:0;bottom:0;width:100%}

  /* phone */
  .phone{left:12px;top:80px;width:40px;height:100px;border-radius:6px;background:#222;padding:10px 3px}
  .phone .screen{width:100%;height:100%;display:flex;align-items:center;justify-content:center}
  .phone .brand{color:#fff;font-size:3px}

  /* business cards */
  .card{width:58px;height:34px;background:var(--paper);font-size:3px;overflow:hidden}
  .card.front{padding:4px}
  .card.front .brand{color:var(--blue);font-size:4px}
  .card.front .name{margin-top:4px;font-weight:700;color:var(--navy)}
  .card.front .lines{margin-top:2px;line-height:1.35;color:var(--muted);font-size:2.4px}
  .card.back{display:flex;align-items:center;justify-content:center}
  .card.back .brand{color:#fff;font-size:4px}

  /* letterhead */
  .letter{width:132px;height:200px;top:14px;background:var(--paper);padding:12px 12px;overflow:hidden}
  .letter .brand{color:var(--blue);font-size:5px;justify-content:center}
  .letter .body{margin-top:26px;font-size:2.6px;line-height:1.6;color:var(--ink)}
  .letter .body p{margin-bottom:3px}
  .letter .foot{position:absolute;left:0;right:0;bottom:3px;text-align:center;font-size:2.2px;color:#fff;white-space:nowrap}

  /* envelopes */
  .env{width:130px;height:58px;background:var(--paper);overflow:hidden}
  .env .brand{position:absolute;left:6px;top:6px;color:var(--blue);font-size:4px}
  .env.back{background:#f3f4f7}
  .env.back .flap{position:absolute;left:0;top:0;width:100%;height:100%}

  /* slips */
  .slip{width:78px;height:26px;background:var(--paper);overflow:hidden}
  .slip .brand{position:absolute;left:5px;top:5px;color:var(--blue);font-size:3.5px}
  .slip.dark .brand{color:#fff}

  /* cd */
  .cd{left:792px;top:90px;width:82px;height:82px;border-radius:50%;display:flex;align-items:center;justify-content:center;flex-direction:column}
  .cd .hole{width:18px;height:18px;border-radius:50%;background:var(--bg);border:4px solid #d7dbe2}
  .cd .brand{color:#fff;font-size:3.5px;margin-top:4px}

  /* pen */
  .pen{left:905px;top:40px;width:6px;height:110px;border-radius:3px;transform:rotate(22deg);background:linear-gradient(90deg,var(--navy),var(--light),var(--navy))}

  /* folder */
  .folder{left:980px;top:12px;width:210px;height:206px;background:var(--paper);display:flex}
  .folder .panel{flex:1;position:relative;overflow:hidden}
  .folder .panel + .panel{border-left:1px solid #e2e4ea}
  .folder .brand{position:absolute;top:60px;left:0;right:0;justify-content:center;color:var(--blue);font-size:6px}
  .folder .web{position:absolute;bottom:14px;left:0;right:0;text-align:center;font-size:2.6px;color:#fff}

  /* shared blue fill, placed last so it wins over white paper */
  .item.blue-grad,.screen.blue-grad{background:linear-gradient(135deg,var(--light),var(--blue) 45%,var(--deep))}
</style>
</head>
<body>

  <div class="item phone">
    <div class="screen blue-grad">
      <div class="brand"><span class="dot" style="width:3px;height:3px"></span>Kelmor Construct</div>
    </div>
  </div>

  <div class="item card back blue-grad" style="left:64px;top:30px">
    <div class="brand"><span class="dot" style="width:4px;height:4px"></span>Kelmor Construct</div>
  </div>
  <div class="item card front" style="left:128px;top:30px">
    <div class="brand"><span class="dot" style="width:4px;height:4px"></span>Kelmor Construct</div>
    <div class="name">Dean T. Haskel</div>
    <div class="lines">President<br>12 Example Lane, Springdale, ST 00000<br>Dean@kelmorconstructinc.example</div>
  </div>
  <div class="item card front" style="left:64px;top:78px">
    <div class="brand"><span class="dot" style="width:4px;height:4px"></span>Kelmor Construct</div>
    <div class="name">Dean T. Haskel</div>
    <div class="lines">President<br>www.kelmorconstructinc.example</div>
  </div>
  <div class="item card back blue-grad" style="left:128px;top:78px">
    <div class="brand"><span class="dot" style="width:4px;height:4px"></span>Kelmor Construct</div>
  </div>
  <div class="item card front" style="left:96px;top:126px">
    <div class="brand"><span class="dot" style="width:4px;height:4px"></span>Kelmor Construct</div>
    <div class="name">Dean T. Haskel</div>
    <div class="lines">President<br>Dean@kelmorconstructinc.example</div>
  </div>

  <div class="item letter" style="left:204px">
    <div class="brand"><span class="dot" style="width:5px;height:5px"></span>Kelmor Construct Inc.</div>
    <div class="body">
      <p>Dear Client,</p>
      <p>Thank you for choosing us to build your next project with care.</p>
      <p>We value honesty, strength and lasting partnership in every job.</p>
      <p>Our team will contact you soon to plan the next steps.</p>
      <p>Sincerely,<br>Dean T. Haskel</p>
    </div>
    <svg class="swoosh" viewBox="0 0 132 20" height="20" preserveAspectRatio="none">
      <path d="M0 10 Q66 -2 132 8 L132 20 L0 20Z" fill="var(--blue)"/>
      <path d="M0 14 Q66 4 132 12 L132 20 L0 20Z" fill="var(--navy)"/>
    </svg>
    <div class="foot">12 Example Lane, Springdale, ST 00000 · www.kelmorconstructinc.example</div>
  </div>

  <div class="item letter" style="left:344px">
    <div class="brand"><span class="dot" style="width:5px;height:5px"></span>Kelmor Construct Inc.</div>
    <svg class="swoosh" viewBox="0 0 132 20" height="20" preserveAspectRatio="none">
      <path d="M0 10 Q66 -2 132 8 L132 20 L0 20Z" fill="var(--blue)"/>
      <path d="M0 14 Q66 4 132 12 L132 20 L0 20Z" fill="var(--navy)"/>
    </svg>
    <div class="foot">12 Example Lane, Springdale, ST 00000 · www.kelmorconstructinc.example</div>
  </div>

  <div class="item env" style="left:486px;top:62px">
    <div class="brand"><span class="dot" style="width:4px;height:4px"></span>Kelmor Construct Inc.</div>
    <svg class="swoosh" viewBox="0 0 130 12" height="12" preserveAspectRatio="none">
      <path d="M0 6 Q65 -1 130 5 L130 12 L0 12Z" fill="var(--blue)"/>
    </svg>
  </div>
  <div class="item env back" style="left:486px;top:128px">
    <svg class="flap" viewBox="0 0 130 58" preserveAspectRatio="none">
      <path d="M0 0 L65 32 L130 0Z" fill="var(--blue)"/>
    </svg>
  </div>

  <div class="item slip" style="left:628px;top:86px">
    <div class="brand"><span class="dot" style="width:3px;height:3px"></span>Kelmor Construct</div>
    <svg class="swoosh" viewBox="0 0 78 8" height="8" preserveAspectRatio="none"><path d="M0 4 Q39 0 78 3 L78 8 L0 8Z" fill="var(--blue)"/></svg>
  </div>
  <div class="item slip dark blue-grad" style="left:710px;top:86px">
    <div class="brand"><span class="dot" style="width:3px;height:3px"></span>Kelmor Construct</div>
  </div>
  <div class="item slip" style="left:628px;top:118px">
    <div class="brand"><span class="dot" style="width:3px;height:3px"></span>Kelmor Construct</div>
    <svg class="swoosh" viewBox="0 0 78 8" height="8" preserveAspectRatio="none"><path d="M0 4 Q39 0 78 3 L78 8 L0 8Z" fill="var(--blue)"/></svg>
  </div>
  <div class="item slip dark blue-grad" style="left:710px;top:118px">
    <div class="brand"><span class="dot" style="width:3px;height:3px"></span>Kelmor Construct</div>
  </div>

  <div class="item cd blue-grad">
    <div class="hole"></div>
    <div class="brand">Company Profile</div>
  </div>

  <div class="item pen"></div>

  <div class="item folder">
    <div class="panel">
      <svg class="swoosh" viewBox="0 0 105 30" height="30" preserveAspectRatio="none">
        <path d="M0 14 Q52 0 105 10 L105 30 L0 30Z" fill="var(--blue)"/>
        <path d="M0 20 Q52 8 105 16 L105 30 L0 30Z" fill="var(--navy)"/>
      </svg>
    </div>
    <div class="panel">
      <div class="brand"><span class="dot" style="width:6px;height:6px"></span>Kelmor Construct Inc.</div>
      <svg class="swoosh" viewBox="0 0 105 30" height="30" preserveAspectRatio="none">
        <path d="M0 14 Q52 0 105 10 L105 30 L0 30Z" fill="var(--blue)"/>
        <path d="M0 20 Q52 8 105 16 L105 30 L0 30Z" fill="var(--navy)"/>
      </svg>
      <div class="web">www.kelmorconstructinc.example</div>
    </div>
  </div>

</body>
</html>
```